Marlow Realty Real Estate Brokerage Recruiting Flyer

We are a real estate brokerage looking to hire more real estate agents. We need to list everything we have to offer as a company so real estate agents will join our company. this is our company website: www.Marlowrealty.example .

100% COMMISSION NO MONTHLY FEE
$450 Flat Transaction FEE

What We Offer:
24/7 Office Access
Free E & O Insurance for 1st Year
Free Online CE and PLE
Free 1,000 Business Cards
Free Professional Social Media Marketing
Free Printing, Scanning, and Copies
Free Buyer and Seller Presentation Packages
Free Filquay Cloud Based Document Management Access
Access to our Internal Brokerage Forum
Company Profit Sharing!
Private Offices Available to Rent

*Lead Generation Software with over 3,000 Leads
*10 Leads to Start
* Free Personal CRM and Website
*Restrictions and Rules apply

Company Address:
4817 Amberfield Road
Suite 512
Fairfax, VA 22194
Phone: 703-555-0147
email: info@marlowrealty.example

Target Market(s)

Real Estate Agents

Industry/Entity Type

Real Estate

Colors
0555a3
ffffff

Requirements
Must have
• 100% COMMISSION NO MONTHLY FEE
$450 Flat Transaction FEE

What We Offer:
24/7 Office Access
Free Online CE and PLE
Free 1,000 Business Cards
Company Profit Sharing!

*10 Leads to Start

Company Address:
4817 Amberfield Road
Suite 512
Fairfax, VA 22194
Phone: 703-555-0147

```html
<!DOCTYPE html>
<html lang="en">
<head>
<meta charset="utf-8">
<title>Marlow Realty – Agent Recruiting Flyer</title>
<link rel="stylesheet" href="https://fonts.googleapis.com/css2?family=Roboto:wght@400;500;700&family=Roboto+Condensed:ital,wght@0,700;1,700&family=Oswald:wght@500;600&display=swap">
<style>
  :root {
    --brand-blue: #0555a3;
    --deep-blue: #0a3f86;
    --navy: #0b2a6b;
    --white: #ffffff;
    --yellow: #f2e320;
    --orange: #f7861e;
    --ink: #2a2a2a;
    --text-grey: #4d4d4d;
    --soft-grey: #e4e5e8;
    --footer-dark: #1f1f21;
    --backdrop: #343434;
  }
  * { margin: 0; padding: 0; box-sizing: border-box; }
  html, body { width: 1145px; height: 1200px; overflow: hidden; background: var(--backdrop); }
  .flyer {
    position: absolute; left: 136px; top: 0;
    width: 749px; height: 1030px;
    transform: scale(1.1651); transform-origin: 0 0;
    background: var(--white);
    font-family: "Roboto", Arial, sans-serif;
    overflow: hidden;
  }
  .shapes { position: absolute; inset: 0; }
  .brand {
    position: absolute; left: 30px; top: 34px; width: 315px; height: 136px;
    display: flex; align-items: center; gap: 14px; padding-left: 16px;
  }
  .brand-mark { width: 26px; height: 26px; background: var(--brand-blue); }
  .brand-name { font-family: "Roboto", Arial, sans-serif; font-weight: 500; font-size: 36px; color: var(--brand-blue); letter-spacing: 1px; }
  .website { position: absolute; right: 43px; top: 54px; font-size: 20px; color: var(--navy); font-weight: 700; letter-spacing: -0.3px; white-space: nowrap; text-align: right; }
  .website .soft { font-weight: 400; font-size: 17px; }
  .headline { position: absolute; font-family: "Oswald", "Roboto Condensed", sans-serif; font-weight: 500; color: var(--white); white-space: nowrap; }
  .headline .accent { color: var(--yellow); font-weight: 600; }
  .headline-commission { left: 36px; top: 236px; font-size: 24px; }
  .headline-commission .accent { font-size: 40px; }
  .headline-commission .pct { font-size: 24px; margin-right: 6px; }
  .headline-fee { left: 98px; top: 282px; font-size: 24px; }
  .headline-fee .accent { font-size: 46px; margin-right: 8px; }
  .headline-fee .dollar { font-size: 28px; }
  .offer-title { position: absolute; left: 48px; top: 393px; font-family: "Roboto Condensed", sans-serif; font-style: italic; font-weight: 700; font-size: 35px; color: var(--orange); }
  .offer-list { position: absolute; left: 108px; top: 455px; list-style: none; }
  .offer-list li { position: relative; padding-left: 20px; font-size: 18px; line-height: 22.4px; color: var(--text-grey); white-space: nowrap; }
  .offer-list li::before { content: ""; position: absolute; left: 0; top: 7px; border-left: 8px solid #8c8c8c; border-top: 5px solid transparent; border-bottom: 5px solid transparent; }
  .offer-list b { color: var(--ink); font-weight: 700; }
  .offer-list i { font-weight: 700; color: var(--ink); }
  .leads { position: absolute; left: 118px; top: 738px; color: var(--ink); }
  .leads h2 { font-size: 21px; font-weight: 700; line-height: 23px; }
  .leads ul { list-style: none; margin-top: 6px; }
  .leads li { font-size: 18px; line-height: 23px; color: var(--text-grey); position: relative; padding-left: 12px; white-space: nowrap; }
  .leads li::before { content: ""; position: absolute; left: 0; top: 8px; border-left: 6px solid var(--ink); border-top: 4px solid transparent; border-bottom: 4px solid transparent; }
  .rules { position: absolute; left: 510px; top: 742px; font-size: 24px; font-weight: 700; line-height: 26px; color: var(--ink); }
  .address-label { position: absolute; left: 110px; top: 928px; font-family: "Roboto Condensed", sans-serif; font-style: italic; font-weight: 700; font-size: 22px; color: var(--orange); }
  .address { position: absolute; left: 110px; top: 956px; font-size: 15px; line-height: 20px; color: var(--white); font-style: normal; }
  .contact { position: absolute; left: 405px; top: 940px; font-size: 15.5px; line-height: 22.5px; color: var(--white); white-space: nowrap; }
  .contact p { padding-left: 23px; }
</style>
</head>
<body>
<main class="flyer">
  <svg class="shapes" viewBox="0 0 749 1030" width="749" height="1030">
    <defs>
      <linearGradient id="blueBand" x1="0" y1="0" x2="1" y2="1">
        <stop offset="0" stop-color="#0a4a9c"/>
        <stop offset="0.5" stop-color="#0555a3"/>
        <stop offset="1" stop-color="#083d85"/>
      </linearGradient>
      <linearGradient id="houseTones" x1="0" y1="0" x2="0" y2="1">
        <stop offset="0" stop-color="#d9dde2"/>
        <stop offset="0.55" stop-color="#a9a49a"/>
        <stop offset="0.8" stop-color="#4f8a3a"/>
        <stop offset="1" stop-color="#3f7a2e"/>
      </linearGradient>
      <linearGradient id="greyPanel" x1="0" y1="0" x2="0" y2="1">
        <stop offset="0" stop-color="#e9eaed"/>
        <stop offset="1" stop-color="#dcdde1"/>
      </linearGradient>
      <linearGradient id="footerDark" x1="0" y1="0" x2="0" y2="1">
        <stop offset="0" stop-color="#3a3a3c"/>
        <stop offset="1" stop-color="#1c1c1e"/>
      </linearGradient>
      <linearGradient id="offerTab" x1="0" y1="0" x2="0" y2="1">
        <stop offset="0" stop-color="#3d3d3f"/>
        <stop offset="1" stop-color="#141414"/>
      </linearGradient>
    </defs>

    <rect x="0" y="380" width="749" height="340" fill="url(#greyPanel)"/>

    <g fill="none" stroke="#c9cbcf" stroke-width="5">
      <circle cx="490" cy="64" r="38"/>
      <ellipse cx="490" cy="64" rx="16" ry="38"/>
      <line x1="452" y1="64" x2="528" y2="64"/>
      <line x1="458" y1="44" x2="522" y2="44"/>
      <line x1="458" y1="84" x2="522" y2="84"/>
    </g>
    <path d="M500 74 L500 108 L508 100 L515 114 L521 111 L514 97 L525 97 Z" fill="#c9cbcf" stroke="#fff" stroke-width="2"/>

    <path d="M0 158 C150 232 300 232 450 182 C560 144 650 115 749 118 L749 132 C650 130 560 158 450 196 C300 246 150 246 0 176 Z" fill="#c8cacd"/>
    <path d="M0 170 C150 244 300 244 450 194 C560 156 650 128 749 130 L749 425 C650 445 540 452 450 425 L300 392 L0 392 Z" fill="url(#blueBand)"/>

    <path role="img" aria-label="Photo of a two-storey suburban house with a red front door, flag and landscaped garden" d="M405 245 L565 110 L749 150 L749 412 C650 432 540 440 455 418 L405 402 Z" fill="url(#houseTones)"/>
    <path d="M380 420 C500 455 640 450 749 405 L749 420 C640 468 500 472 380 430 Z" fill="#bfc1c5"/>

    <path d="M0 390 L270 390 A25 25 0 0 1 270 440 L0 440 Z" fill="url(#offerTab)"/>

    <rect x="0" y="720" width="749" height="180" fill="#ffffff"/>
    <path d="M398 720 L432 720 L415 738 Z" fill="#dcdde1"/>

    <rect role="img" aria-label="Faded photo of a large white house" x="330" y="722" width="419" height="190" fill="#eef0f2" opacity="0.9"/>

    <g fill="none" stroke="var(--orange)" stroke-width="2.5">
      <circle cx="68" cy="755" r="22"/>
      <circle cx="68" cy="758" r="10"/>
      <circle cx="68" cy="758" r="3"/>
      <rect x="38" y="775" width="60" height="28" rx="4"/>
      <line x1="44" y1="795" x2="92" y2="795" stroke-dasharray="3 2"/>
    </g>
    <g fill="none" stroke="var(--orange)" stroke-width="2.5">
      <circle cx="465" cy="770" r="31"/>
      <path d="M462 784 L462 758 a4 4 0 0 1 8 0 L470 772 L480 774 a5 5 0 0 1 4 6 L481 795 L462 795 L452 780 a4 4 0 0 1 7 -4 Z"/>
      <line x1="444" y1="749" x2="486" y2="791"/>
    </g>

    <path d="M0 895 C120 860 260 872 420 890 C560 905 680 880 749 840 L749 850 C680 892 560 918 420 902 C260 884 120 872 0 905 Z" fill="#9b9ca0"/>
    <path d="M0 903 C120 870 260 882 420 900 C560 915 680 890 749 848 L749 1030 L0 1030 Z" fill="url(#footerDark)"/>
    <line x1="355" y1="958" x2="355" y2="1010" stroke="#777" stroke-width="2"/>

    <g fill="none" stroke="#ffffff" stroke-width="2.2">
      <path d="M68 978 C56 962 50 954 50 944 a18 18 0 0 1 36 0 C86 954 80 962 68 978 Z"/>
      <circle cx="68" cy="944" r="7"/>
      <path d="M56 968 L42 988 L96 988 L82 968"/>
      <line x1="49" y1="978" x2="89" y2="978"/>
    </g>
    <path transform="translate(405 943) scale(0.72) translate(-408 -942)" d="M408 942 c2 -2 4 -2 5 0 l2 3 c1 2 0 3 -1 4 c1 3 3 5 6 6 c1 -1 2 -2 4 -1 l3 2 c2 1 2 3 0 5 c-3 3 -8 2 -13 -3 c-5 -5 -8 -11 -6 -16 Z" fill="var(--orange)"/>
    <g fill="none" stroke="var(--orange)" stroke-width="1.6">
      <rect x="405" y="968" width="15" height="11"/>
      <path d="M405 968 L412.5 974 L420 968"/>
    </g>
  </svg>

  <div class="brand">
    <span class="brand-mark"></span>
    <span class="brand-name">Marlow Realty</span>
  </div>
  <p class="website">www.<span>Marlowrealty</span><span class="soft">.example</span></p>

  <p class="headline headline-commission"><span class="accent">100</span><span class="accent pct">%</span>Commission no monthly Fee</p>
  <p class="headline headline-fee"><span class="accent"><span class="dollar">$</span>450</span>Flat Transaction Fee</p>

  <h1 class="offer-title">What We Offer:</h1>
  <ul class="offer-list">
    <li><i>24/7</i> Office Access</li>
    <li><b>Free</b> E &amp; O Insurance for 1st Year</li>
    <li><b>Free</b> Online CE and PLE</li>
    <li><b>Free</b> 1,000 Business Cards</li>
    <li><b>Free</b> Professional Social Media Marketing</li>
    <li><b>Free</b> Printing, Scanning, and Copies</li>
    <li><b>Free</b> Buyer and Seller Presentation Packages</li>
    <li><b>Free</b> Filquay Cloud Based Document Management Access</li>
    <li>Access to our <b>Internal Brokerage Forum</b></li>
    <li>Company Profit Sharing!</li>
    <li>Private Offices Available to Rent</li>
  </ul>

  <section class="leads">
    <h2>Lead Generation Software<br>with over 3,000 Leads</h2>
    <ul>
      <li>10 Leads to Start</li>
      <li>Free Personal CRM and Website</li>
    </ul>
  </section>
  <p class="rules">Restrictions and<br>Rules apply</p>

  <h3 class="address-label">Company Address:</h3>
  <address class="address">4817 Amberfield Road<br>Suite 512 Fairfax, VA 22194</address>
  <div class="contact">
    <p>Phone: 703-555-0147</p>
    <p>Email: info@marlowrealty.example</p>
    <p>Licensed in D.C., Maryland, and Virginia</p>
  </div>
</main>
</body>
</html>
```